App Redesign for PathMentor

We're looking for a skilled UI/UX designer to modernize the PathMentor mobile app, enhancing user engagement while preserving our current brand identity.

Key Objectives:
Refresh the app using modern design trends
Maintain a clean, calm, and playful aesthetic aligned with our brand
Boost engagement through improved flow, visuals, and interactivity

Design Requirements:
Retain recognizability from our app and website (see Brand ID Guide) (and website pathmentorhub.example)
Reflect a tone that is supportive, fun/ playful, and professional

Design 5–8 key screens, including:
Home/Dashboard
Daily Intentions Interface
Gamification Overview (Streaks, Rewards)
Social Features (Direct Realtime Feedback, Messaging, Challenges)
Progress Tracking

New Feature Concepts to Include:
Daily Intentions with voice/text input and visual encouragement
Gamification elements like streaks, badges, and animations
Social Connections including messaging, reactions, and feedback tools
Optional: Subtle design cues for future AI-driven interactions

Audience: Adults aged 25–55 interested in personal development and coaching. Tech-comfortable but not tech-savvy.

Visual Inspiration: Lexaroo (gamification), Calmnook (intentions), Pacely (social support)

Target Market(s)

Corporate Leaders and Entrepreneurs

Industry/Entity Type

Leadership Training & Consultancies

Font styles to use
Sans Serif
Other font styles liked:
• Avenir, Arial

Colors
FFF300
FFF600
FEFA6F
FFFEC7
FFFEE8

Requirements
Nice to have
• Lexaroo, Calmnook,

```html
<!DOCTYPE html>
<html lang="en">
<head>
<meta charset="utf-8">
<title>PathMentor – App Screens</title>
<link href="https://fonts.googleapis.com/css2?family=Mulish:wght@400;500;600;700;800&display=swap" rel="stylesheet">
<style>
:root{
  --yellow:#FFD500;
  --gold:#F7C600;
  --cream:#FFF7CF;
  --cream-soft:#FFFBE6;
  --ink:#111111;
  --grey:#9A9A9A;
  --grey-bubble:#E3E3E3;
  --nav-end:#CFC4BC;
  --line:#9C9C9C;
  --white:#FFFFFF;
}
*{box-sizing:border-box;margin:0;padding:0}
html,body{width:1182px;height:1200px;overflow:hidden;background:var(--white)}
body{position:relative;font-family:'Mulish',Arial,sans-serif;color:var(--ink)}
.phone{position:absolute;width:347px;background:var(--white);box-shadow:0 0 0 1px #EEEEEE;overflow:hidden}
.phone--home{left:44px;top:46px;height:1109px}
.phone--intentions{left:418px;top:46px;height:747px}
.phone--social{left:793px;top:46px;height:747px}
.abs{position:absolute}
.status{position:absolute;left:0;top:18px;width:100%;height:20px;font-size:13px}
.status__time{position:absolute;left:13px;top:2px}
.brand{position:absolute;left:82px;top:0;display:flex;align-items:center;gap:6px;font-size:14px;font-weight:700;color:var(--gold)}
.brand__dot{width:12px;height:12px;border-radius:50%;background:var(--yellow)}
.status__icons{position:absolute;right:14px;top:3px}
.screen-title{position:absolute;left:0;width:100%;text-align:center;font-size:19px;font-weight:600;color:var(--gold)}
.screen-title .muted{color:var(--grey)}
.card{position:absolute;left:21px;width:305px;background:var(--cream);border-radius:8px}
.report{display:flex;align-items:center;font-size:15px;font-weight:700}
.report__icon{position:absolute;left:18px;top:12px}
.report__num{position:absolute;left:104px;font-size:19px;font-weight:600}
.report__label{position:absolute;left:173px}
.axis{font-size:9px;fill:var(--ink);font-family:'Mulish',Arial,sans-serif}
.nav{position:absolute;left:0;width:100%;height:50px;background:var(--yellow);border-top-left-radius:26px;display:flex;align-items:center;padding-left:16px;font-size:10.5px;font-weight:700;white-space:nowrap}
.nav__item{color:var(--ink)}
.nav__item--active{color:var(--white)}
.nav__sep{margin:0 6px;color:var(--ink)}
.nav__menu{position:absolute;right:0;top:0;width:38px;height:50px;background:var(--nav-end);border-top-right-radius:26px;display:flex;align-items:center;justify-content:center}
.prompt{font-size:16px;font-weight:600;text-align:center;top:16px;width:100%;position:absolute}
.field{position:absolute;left:45px;top:151px;width:258px;height:38px;background:var(--white);border:1px solid #E2E2E2;border-radius:6px;font-size:13px;color:#666;padding:11px 14px}
.field svg{position:absolute;right:14px;top:10px}
.entry{position:absolute;left:48px;font-size:12px;font-weight:500;white-space:nowrap;letter-spacing:-0.1px}
.entry-icon{position:absolute;left:17px}
.dots{position:absolute;top:193px;left:0;width:100%;display:flex;justify-content:center;gap:12px}
.dots span{width:8px;height:8px;border-radius:50%;border:1.2px solid var(--gold)}
.dots span.on{background:var(--gold)}
.timer-label{position:absolute;top:26px;font-size:13px;font-weight:600;transform:translateX(-50%)}
.timer-pill{position:absolute;top:50px;width:30px;height:30px;border-radius:50%;background:var(--white);font-size:13px;font-weight:600;display:flex;align-items:center;justify-content:center;transform:translateX(-50%)}
.timer-colon{position:absolute;top:56px;font-size:13px;font-weight:700}
.btn{position:absolute;left:176px;top:98px;width:68px;height:22px;border-radius:11px;background:var(--yellow);font-size:11px;font-weight:700;display:flex;align-items:center;justify-content:center}
.chat-panel{position:absolute;left:18px;top:89px;width:311px;height:640px;background:var(--cream);border-radius:40px 40px 0 0}
.avatar{position:absolute;border-radius:50%}
.avatar--photo{left:26px;top:20px;width:50px;height:50px;background:radial-gradient(circle at 50% 40%,#E9C4B2,#F3B6C0)}
.avatar--blank{width:40px;height:40px;background:#CFCFCF}
.contact{position:absolute;left:98px;top:35px;font-size:16px;font-weight:700}
.bubble{position:absolute;font-size:13px;line-height:20px;font-weight:500;padding:9px 12px;border-radius:18px}
.bubble--in{background:var(--grey-bubble)}
.bubble--out{background:var(--yellow)}
.composer{position:absolute;left:9px;top:474px;width:291px;height:170px;background:var(--white);border-radius:8px}
.composer__hint{position:absolute;left:42px;top:14px;font-size:13.5px;color:#888}
.emoji-set{position:absolute;left:17px;top:46px;width:262px;height:94px;border-radius:6px;background:linear-gradient(180deg,#FFE36A,#FFD23F)}
</style>
</head>
<body>

<!-- Home / Progress -->
<section class="phone phone--home">
  <div class="status">
    <span class="status__time">4:28</span>
    <span class="brand"><span class="brand__dot"></span>PathMentor</span>
    <svg class="status__icons" width="62" height="12" viewBox="0 0 62 12"><rect x="0" y="8" width="2" height="3"/><rect x="3" y="6" width="2" height="5"/><rect x="6" y="3" width="2" height="8"/><path d="M22 10l2-2a3 3 0 0 0-4 0z M18 6a6 6 0 0 1 8 0l-1 1a4.5 4.5 0 0 0-6 0z" /><rect x="42" y="2" width="16" height="9" rx="1.5" fill="none" stroke="#111"/><rect x="44" y="4" width="8" height="5"/><rect x="58.5" y="5" width="1.5" height="3"/></svg>
  </div>
  <h1 class="screen-title" style="top:69px">BrightMind™ <span class="muted">Tracker</span></h1>

  <div class="card report" style="top:109px;height:49px">
    <svg class="report__icon" width="28" height="28" viewBox="0 0 28 28"><circle cx="12" cy="12" r="10" fill="var(--yellow)"/><path d="M12 12V2A10 10 0 0 1 22 12z" fill="#FFE880"/><rect x="14" y="16" width="12" height="11" fill="var(--yellow)" stroke="#fff" stroke-width="1.5"/></svg>
    <span class="report__num" style="top:13px">271</span>
    <span class="report__label" style="top:15px">Weekly Reports</span>
  </div>
  <div class="card report" style="top:171px;height:49px">
    <svg class="report__icon" width="32" height="28" viewBox="0 0 32 28"><rect x="1" y="18" width="7" height="9" fill="var(--yellow)"/><rect x="11" y="14" width="7" height="13" fill="var(--yellow)"/><rect x="21" y="10" width="7" height="17" fill="var(--yellow)"/><path d="M2 13l10-5 6 2 10-8" stroke="var(--yellow)" stroke-width="2.5" fill="none"/></svg>
    <span class="report__num" style="top:13px">75</span>
    <span class="report__label" style="top:15px">Monthly Reports</span>
  </div>

  <h2 class="screen-title" style="top:248px">Your Overall <span class="muted">Progress</span></h2>
  <div class="card" style="top:291px;height:215px">
    <svg width="305" height="215" viewBox="0 0 305 215">
      <g stroke="var(--line)" stroke-width="0.8">
        <line x1="44" y1="33" x2="291" y2="33"/><line x1="44" y1="64" x2="291" y2="64"/><line x1="44" y1="96" x2="291" y2="96"/><line x1="44" y1="128" x2="291" y2="128"/><line x1="44" y1="160" x2="291" y2="160"/><line x1="44" y1="191" x2="291" y2="191"/>
      </g>
      <g class="axis"><text x="13" y="37" style="font-size:11px">100</text><text x="19" y="68" style="font-size:11px">80</text><text x="19" y="100" style="font-size:11px">60</text><text x="19" y="132" style="font-size:11px">40</text><text x="19" y="164" style="font-size:11px">20</text><text x="25" y="195" style="font-size:11px">0</text></g>
      <polyline points="38,117 62,108 85,124 108,131 130,137 153,139 177,126 201,137 223,133 248,134 270,138 295,134" fill="none" stroke="var(--yellow)" stroke-width="1.2" stroke-dasharray="3 2"/>
      <g fill="#C9C0B4"><circle cx="38" cy="117" r="2.2"/><circle cx="62" cy="108" r="2.2"/><circle cx="85" cy="124" r="2.2"/><circle cx="108" cy="131" r="2.2"/><circle cx="130" cy="137" r="2.2"/><circle cx="153" cy="139" r="2.2"/><circle cx="177" cy="126" r="2.2"/><circle cx="201" cy="137" r="2.2"/><circle cx="223" cy="133" r="2.2"/><circle cx="248" cy="134" r="2.2"/><circle cx="270" cy="138" r="2.2"/><circle cx="295" cy="134" r="2.2"/></g>
    </svg>
  </div>

  <h2 class="screen-title" style="top:528px;line-height:30px">BODY: Did I take a cold shower<br><span class="muted">or swim in the river today?</span></h2>
  <div class="card" style="top:602px;height:166px">
    <svg width="305" height="166" viewBox="0 0 305 166">
      <g stroke="var(--line)" stroke-width="0.7">
        <line x1="32" y1="18" x2="294" y2="18"/><line x1="32" y1="29" x2="294" y2="29"/><line x1="32" y1="40" x2="294" y2="40"/><line x1="32" y1="51" x2="294" y2="51"/><line x1="32" y1="62" x2="294" y2="62"/><line x1="32" y1="73" x2="294" y2="73"/><line x1="32" y1="84" x2="294" y2="84"/><line x1="32" y1="95" x2="294" y2="95"/><line x1="32" y1="106" x2="294" y2="106"/><line x1="32" y1="117" x2="294" y2="117"/><line x1="32" y1="128" x2="294" y2="128"/>
      </g>
      <g class="axis" style="font-size:8px"><text x="9" y="21">5.0</text><text x="9" y="32">4.5</text><text x="9" y="43">4.0</text><text x="9" y="54">3.5</text><text x="9" y="65">3.0</text><text x="9" y="76">2.5</text><text x="9" y="87">2.0</text><text x="9" y="98">1.5</text><text x="9" y="109">1.0</text><text x="9" y="120">0.5</text><text x="15" y="131">0</text></g>
      <polyline points="41,106 53,106 64,106 76,84 87,104 99,84 111,84 122,84 134,73 145,57 157,40 169,84 180,104 192,104 203,84 215,84 227,84 238,104 250,84 261,104 273,62 285,104" fill="none" stroke="var(--yellow)" stroke-width="1.2" stroke-dasharray="3 2"/>
      <g fill="#C9C0B4"><circle cx="41" cy="106" r="2"/><circle cx="64" cy="106" r="2"/><circle cx="76" cy="84" r="2"/><circle cx="87" cy="104" r="2"/><circle cx="99" cy="84" r="2"/><circle cx="122" cy="84" r="2"/><circle cx="157" cy="40" r="2"/><circle cx="169" cy="84" r="2"/><circle cx="180" cy="104" r="2"/><circle cx="192" cy="104" r="2"/><circle cx="203" cy="84" r="2"/><circle cx="227" cy="84" r="2"/><circle cx="238" cy="104" r="2"/><circle cx="250" cy="84" r="2"/><circle cx="261" cy="104" r="2"/><circle cx="273" cy="62" r="2"/><circle cx="285" cy="104" r="2"/></g>
      <g class="axis" style="font-size:8px;font-weight:700">
        <text transform="translate(44,160) rotate(-90)">WK 50</text><text transform="translate(63,150) rotate(-90)">WK 1</text><text transform="translate(83,150) rotate(-90)">WK 3</text><text transform="translate(106,150) rotate(-90)">WK 5</text><text transform="translate(128,150) rotate(-90)">WK 7</text><text transform="translate(151,150) rotate(-90)">WK 9</text><text transform="translate(170,155) rotate(-90)">WK 11</text><text transform="translate(192,155) rotate(-90)">WK 13</text><text transform="translate(211,155) rotate(-90)">WK 15</text><text transform="translate(235,155) rotate(-90)">WK 17</text><text transform="translate(258,155) rotate(-90)">WK 19</text><text transform="translate(273,155) rotate(-90)">WK 12</text>
      </g>
    </svg>
  </div>

  <h2 class="screen-title" style="top:795px;line-height:30px">BALANCE: what was focus in<br><span class="muted">family activities?</span></h2>
  <div class="card" style="top:868px;height:168px">
    <svg width="305" height="168" viewBox="0 0 305 168">
      <g stroke="var(--line)" stroke-width="0.7">
        <line x1="30" y1="18" x2="294" y2="18"/><line x1="30" y1="32" x2="294" y2="32"/><line x1="30" y1="47" x2="294" y2="47"/><line x1="30" y1="61" x2="294" y2="61"/><line x1="30" y1="75" x2="294" y2="75"/><line x1="30" y1="89" x2="294" y2="89"/><line x1="30" y1="104" x2="294" y2="104"/><line x1="30" y1="118" x2="294" y2="118"/>
      </g>
      <g class="axis" style="font-size:8px"><text x="16" y="21">7</text><text x="16" y="35">6</text><text x="16" y="50">5</text><text x="16" y="64">4</text><text x="16" y="78">3</text><text x="16" y="92">2</text><text x="16" y="107">1</text><text x="16" y="121">0</text></g>
      <g fill="var(--yellow)">
        <rect x="46" y="33" width="6" height="85"/><rect x="58" y="33" width="6" height="85"/><rect x="70" y="33" width="6" height="85"/><rect x="92" y="33" width="6" height="85"/><rect x="114" y="33" width="6" height="85"/><rect x="136" y="33" width="6" height="85"/><rect x="148" y="19" width="6" height="99"/><rect x="192" y="33" width="6" height="85"/><rect x="204" y="33" width="6" height="85"/><rect x="226" y="29" width="6" height="89"/><rect x="248" y="29" width="6" height="89"/><rect x="270" y="33" width="6" height="85"/><rect x="282" y="18" width="6" height="100"/>
      </g>
      <g fill="#C9C0B4">
        <rect x="81" y="47" width="6" height="71"/><rect x="103" y="37" width="6" height="81"/><rect x="125" y="41" width="6" height="77"/><rect x="159" y="37" width="6" height="81"/><rect x="170" y="41" width="6" height="77"/><rect x="181" y="33" width="6" height="85"/><rect x="215" y="36" width="6" height="82"/><rect x="237" y="33" width="6" height="85"/><rect x="259" y="37" width="6" height="81"/><rect x="292" y="61" width="6" height="57"/>
      </g>
      <g class="axis" style="font-size:8px;font-weight:700">
        <text transform="translate(53,156) rotate(-90)">WK 50</text><text transform="translate(75,150) rotate(-90)">WK 1</text><text transform="translate(95,150) rotate(-90)">WK 3</text><text transform="translate(118,150) rotate(-90)">WK 5</text><text transform="translate(140,150) rotate(-90)">WK 7</text><text transform="translate(162,156) rotate(-90)">WK 10</text><text transform="translate(182,156) rotate(-90)">WK 12</text><text transform="translate(205,156) rotate(-90)">WK 14</text><text transform="translate(227,160) rotate(-90)">WK 156</text><text transform="translate(250,156) rotate(-90)">WK 18</text><text transform="translate(273,156) rotate(-90)">WK 20</text><text transform="translate(288,156) rotate(-90)">WK 12</text>
      </g>
    </svg>
  </div>

  <nav class="nav" style="top:1059px">
    <span class="nav__item nav__item--active">HOME</span><span class="nav__sep">|</span><span class="nav__item">DAILY INTENTIONS</span><span class="nav__sep">|</span><span class="nav__item">GAMIFICATION</span><span class="nav__sep">|</span><span class="nav__item">SOCIAL</span>
    <span class="nav__menu"><svg width="14" height="10" viewBox="0 0 14 10" stroke="#fff" stroke-width="1.6"><line x1="0" y1="1" x2="14" y2="1"/><line x1="0" y1="5" x2="14" y2="5"/><line x1="0" y1="9" x2="14" y2="9"/></svg></span>
  </nav>
</section>

<!-- Daily Intentions -->
<section class="phone phone--intentions">
  <div class="status">
    <span class="status__time">4:28</span>
    <span class="brand"><span class="brand__dot"></span>PathMentor</span>
    <svg class="status__icons" width="62" height="12" viewBox="0 0 62 12"><rect x="0" y="8" width="2" height="3"/><rect x="3" y="6" width="2" height="5"/><rect x="6" y="3" width="2" height="8"/><path d="M22 10l2-2a3 3 0 0 0-4 0z M18 6a6 6 0 0 1 8 0l-1 1a4.5 4.5 0 0 0-6 0z"/><rect x="42" y="2" width="16" height="9" rx="1.5" fill="none" stroke="#111"/><rect x="44" y="4" width="8" height="5"/><rect x="58.5" y="5" width="1.5" height="3"/></svg>
  </div>
  <h1 class="screen-title" style="top:61px">Daily <span class="muted">Intentions</span></h1>
  <div class="card" style="top:99px;height:74px"><p class="prompt">What Will Help You Grow Today?</p></div>
  <div class="field">Enter Intension
    <svg width="10" height="16" viewBox="0 0 10 16"><rect x="2.5" y="0" width="5" height="10" rx="2.5"/><path d="M0.8 7a4.2 4.2 0 0 0 8.4 0" fill="none" stroke="#111" stroke-width="1.2"/><line x1="5" y1="11" x2="5" y2="15" stroke="#111" stroke-width="1.2"/></svg>
  </div>

  <h2 class="screen-title" style="top:214px">Past <span class="muted">Intentions</span></h2>
  <div class="card" style="top:256px;height:215px">
    <svg class="entry-icon" style="top:22px" width="16" height="16" viewBox="0 0 16 16"><rect x="1" y="2" width="14" height="13" fill="#fff" stroke="#E05A4B"/><rect x="1" y="2" width="14" height="4" fill="#E05A4B"/></svg>
    <span class="entry" style="top:22px">Thursday, June 13</span>
    <svg class="entry-icon" style="top:50px" width="18" height="18" viewBox="0 0 18 18"><path d="M9 1l2 6 6 2-6 2-2 6-2-6-6-2 6-2z" fill="var(--yellow)" stroke="#2C3E66" stroke-width="0.8"/></svg>
    <span class="entry" style="top:50px">"Take 5 deep breaths before every meeting"</span>
    <svg class="entry-icon" style="top:77px" width="16" height="18" viewBox="0 0 16 18"><path d="M8 1c1 4 6 6 6 11a6 6 0 0 1-12 0c0-3 2-4 3-6 0 2 1 3 2 3 0-3 0-5 1-8z" fill="#F26A1B"/><path d="M8 10c2 2 3 3 3 4a3 3 0 0 1-6 0c0-1 1-2 3-4z" fill="var(--yellow)"/></svg>
    <span class="entry" style="top:77px">8-Day Streak</span>
    <svg class="entry-icon" style="top:106px" width="18" height="18" viewBox="0 0 18 18"><circle cx="9" cy="9" r="8" fill="var(--yellow)" stroke="#E0A800"/></svg>
    <span class="entry" style="top:106px">Mood: Calm</span>
    <svg class="entry-icon" style="top:133px" width="18" height="16" viewBox="0 0 18 16"><path d="M1 1h16v10H6l-4 4v-4H1z" fill="none" stroke="#333"/><circle cx="6" cy="6" r="0.9"/><circle cx="9" cy="6" r="0.9"/><circle cx="12" cy="6" r="0.9"/></svg>
    <span class="entry" style="top:133px">Note: “Helped me reset after morning stress.”</span>
    <svg class="entry-icon" style="top:162px" width="18" height="16" viewBox="0 0 18 16"><path d="M9 15S1 10 1 5a4 4 0 0 1 8-1 4 4 0 0 1 8 1c0 5-8 10-8 10z" fill="var(--yellow)" stroke="#C9A000"/></svg>
    <span class="entry" style="top:161px">Reflect Again</span>
    <div class="dots"><span class="on"></span><span></span><span></span><span></span></div>
  </div>

  <h2 class="screen-title" style="top:490px">Set a <span class="muted">Timer</span></h2>
  <div class="card" style="top:528px;height:149px">
    <svg class="abs" style="left:36px;top:27px" width="92" height="92" viewBox="0 0 92 92"><circle cx="46" cy="46" r="44" fill="none" stroke="#111" stroke-width="3"/><circle cx="46" cy="46" r="36" fill="none" stroke="#111" stroke-width="2.5"/><g stroke="#111" stroke-width="2"><line x1="46" y1="10" x2="46" y2="18"/><line x1="46" y1="74" x2="46" y2="82"/><line x1="10" y1="46" x2="18" y2="46"/><line x1="74" y1="46" x2="82" y2="46"/><line x1="46" y1="46" x2="64" y2="20"/><line x1="46" y1="46" x2="40" y2="72"/></g><circle cx="46" cy="46" r="3.5"/></svg>
    <svg class="abs" style="left:284px;top:8px" width="18" height="14" viewBox="0 0 18 14" stroke="#111" stroke-width="1.4"><line x1="5" y1="1" x2="18" y2="1"/><line x1="5" y1="7" x2="18" y2="7"/><line x1="5" y1="13" x2="18" y2="13"/><line x1="0" y1="1" x2="2" y2="1"/><line x1="0" y1="7" x2="2" y2="7"/><line x1="0" y1="13" x2="2" y2="13"/></svg>
    <span class="timer-label" style="left:168px">Hrs</span><span class="timer-label" style="left:210px">Min</span><span class="timer-label" style="left:252px">Sec</span>
    <span class="timer-pill" style="left:168px">06</span><span class="timer-colon" style="left:187px">:</span><span class="timer-pill" style="left:210px">30</span><span class="timer-colon" style="left:229px">:</span><span class="timer-pill" style="left:252px">10</span>
    <span class="btn">Set Timer</span>
  </div>

  <nav class="nav" style="top:696px">
    <span class="nav__item nav__item--active">HOME</span><span class="nav__sep">|</span><span class="nav__item">DAILY INTENTIONS</span><span class="nav__sep">|</span><span class="nav__item">GAMIFICATION</span><span class="nav__sep">|</span><span class="nav__item">SOCIAL</span>
    <span class="nav__menu"><svg width="14" height="10" viewBox="0 0 14 10" stroke="#fff" stroke-width="1.6"><line x1="0" y1="1" x2="14" y2="1"/><line x1="0" y1="5" x2="14" y2="5"/><line x1="0" y1="9" x2="14" y2="9"/></svg></span>
  </nav>
</section>

<!-- Social -->
<section class="phone phone--social">
  <div class="status">
    <span class="status__time">4:28</span>
    <span class="brand"><span class="brand__dot"></span>PathMentor</span>
    <svg class="status__icons" width="62" height="12" viewBox="0 0 62 12"><rect x="0" y="8" width="2" height="3"/><rect x="3" y="6" width="2" height="5"/><rect x="6" y="3" width="2" height="8"/><path d="M22 10l2-2a3 3 0 0 0-4 0z M18 6a6 6 0 0 1 8 0l-1 1a4.5 4.5 0 0 0-6 0z"/><rect x="42" y="2" width="16" height="9" rx="1.5" fill="none" stroke="#111"/><rect x="44" y="4" width="8" height="5"/><rect x="58.5" y="5" width="1.5" height="3"/></svg>
  </div>
  <h1 class="screen-title" style="top:51px">Social</h1>
  <div class="chat-panel">
    <div class="avatar avatar--photo" role="img" aria-label="Profile photo of the contact"></div>
    <span class="contact">Lorem Ipsum</span>
    <svg class="abs" style="left:246px;top:38px" width="16" height="16" viewBox="0 0 16 16"><path d="M3 1l3 3-2 2a10 10 0 0 0 6 6l2-2 3 3-2 2C6 15 1 10 1 3z"/></svg>
    <svg class="abs" style="left:279px;top:39px" width="4" height="14" viewBox="0 0 4 14"><circle cx="2" cy="2" r="1.5"/><circle cx="2" cy="7" r="1.5"/><circle cx="2" cy="12" r="1.5"/></svg>

    <div class="avatar avatar--blank" style="left:17px;top:111px"></div>
    <div class="bubble bubble--in" style="left:70px;top:112px;width:126px;height:38px;text-align:center">Lorem ipsum</div>
    <div class="bubble bubble--out" style="left:118px;top:171px;width:176px;height:79px">Lorem ipsum dolor sit amet, consectetur adipiscing elit, sed do</div>
    <div class="avatar avatar--blank" style="left:17px;top:329px"></div>
    <div class="bubble bubble--in" style="left:70px;top:271px;width:176px;height:78px">Lorem ipsum dolor sit amet, consectetur adipiscing elit, sed do</div>
    <div class="bubble bubble--out" style="left:118px;top:369px;width:176px;height:79px">Lorem ipsum dolor sit amet, consectetur adipiscing elit, sed do</div>

    <div class="composer">
      <svg class="abs" style="left:14px;top:16px" width="16" height="16" viewBox="0 0 16 16"><circle cx="8" cy="8" r="7.5" fill="var(--yellow)"/></svg>
      <span class="composer__hint">Type Your Message</span>
      <svg class="abs" style="left:263px;top:18px" width="9" height="14" viewBox="0 0 10 16"><rect x="2.5" y="0" width="5" height="10" rx="2.5"/><path d="M0.8 7a4.2 4.2 0 0 0 8.4 0" fill="none" stroke="#111" stroke-width="1.2"/><line x1="5" y1="11" x2="5" y2="15" stroke="#111" stroke-width="1.2"/></svg>
      <div class="emoji-set" role="img" aria-label="Grid of emoji reactions to pick from"></div>
    </div>
  </div>

  <nav class="nav" style="top:696px">
    <span class="nav__item">HOME</span><span class="nav__sep">|</span><span class="nav__item">DAILY INTENTIONS</span><span class="nav__sep">|</span><span class="nav__item">GAMIFICATION</span><span class="nav__sep">|</span><span class="nav__item nav__item--active">SOCIAL</span>
    <span class="nav__menu"><svg width="14" height="10" viewBox="0 0 14 10" stroke="#fff" stroke-width="1.6"><line x1="0" y1="1" x2="14" y2="1"/><line x1="0" y1="5" x2="14" y2="5"/><line x1="0" y1="9" x2="14" y2="9"/></svg></span>
  </nav>
</section>

</body>
</html>
```